Brand New Solar Energy Business Needs a Flyer Design

We need an A5 double sided flyer for a new company in South Australia called Dorrit & Vale. We install home solar power systems and try to focus on quality of product and install.We also offer solar system servicing for existing systems which includes maintenance, cleaning and safety checks. Our web address is www.dorritandvale.com.au
We would like to see a design that's fresh and stands out in the mail box.
We feel the final design should communicate saving money on your electricity bills, local, quality and safety.
Target Market(s)
Home owners
Industry/Entity Type
Safety
Requirements
Must have
- A reference to our web site www.dorritandvale.com.au
A telephone number 0491638274

```html
<!DOCTYPE html>
<html lang="en">
<head>
<meta charset="utf-8">
<title>Dorrit &amp; Vale – Home Solar Power Systems</title>
<link rel="stylesheet" href="https://fonts.googleapis.com/css2?family=Ubuntu:wght@400;500;700&family=Fredoka:wght@600;700&display=swap">
<style>
  :root {
    --sky-deep: #2b3d8c;
    --sky-mid: #3f74c4;
    --sky-light: #9ccbf0;
    --roof: #b5532c;
    --wall: #e9e6dc;
    --foliage: #6f9a2e;
    --flower: #e8c51c;
    --headline-white: #ffffff;
    --headline-yellow: #ffe000;
    --tagline: #c3cbe4;
    --box-top: #2e8fd8;
    --box-bottom: #0f5ea8;
    --brand-blue: #29a7e1;
    --brand-green: #2f9a3a;
    --ink: #4a4a4a;
    --ink-strong: #333333;
    --paper: #ffffff;
  }
  * { margin: 0; padding: 0; box-sizing: border-box; }
  html, body { width: 856px; height: 1200px; overflow: hidden; background: var(--paper); }
  .flyer { position: relative; width: 856px; height: 1200px; font-family: "Ubuntu", sans-serif; background: var(--paper); overflow: hidden; }

  .hero-photo {
    position: absolute; left: 0; top: 0; width: 856px; height: 948px;
    background:
      radial-gradient(circle at 95px 60px, rgba(255,255,255,0.95) 0 18px, rgba(255,255,255,0.35) 40px, rgba(255,255,255,0) 120px),
      linear-gradient(180deg, var(--sky-deep) 0%, var(--sky-mid) 28%, var(--sky-light) 52%, var(--roof) 62%, #3b5aa0 68%, var(--wall) 76%, var(--foliage) 86%, var(--flower) 94%, var(--foliage) 100%);
  }

  .service-line {
    position: absolute; top: 45px; right: 42px;
    font-weight: 500; font-size: 24px; letter-spacing: 0.3px; color: var(--tagline);
  }

  .headline {
    position: absolute; left: 228px; top: 150px;
    font-family: "Fredoka", sans-serif; font-weight: 700; text-transform: lowercase;
    line-height: 0.78; transform: rotate(-13deg); transform-origin: left top;
  }
  .headline span { display: block; }
  .headline .word-home { font-size: 118px; color: var(--headline-white); }
  .headline .word-solar { font-size: 118px; color: var(--headline-yellow); margin-left: 12px; }
  .headline .word-power { font-size: 118px; color: var(--headline-yellow); margin-left: 22px; }
  .headline .word-systems { font-size: 138px; color: var(--headline-white); margin-left: 30px; }

  .benefits { position: absolute; top: 872px; left: 46px; display: flex; gap: 5px; }
  .benefit {
    height: 76px; border: 2px solid #fff; border-bottom: none; border-radius: 10px 10px 0 0;
    background: linear-gradient(180deg, var(--box-top), var(--box-bottom));
    color: #fff; text-align: center; font-size: 16px; line-height: 19px;
    display: flex; align-items: center; justify-content: center; padding: 0 6px;
  }
  .benefit b { font-weight: 700; }
  .benefit-free { width: 160px; }
  .benefit-affordable { width: 182px; }
  .benefit-bills { width: 250px; }
  .benefit-emissions { width: 158px; }

  .brand { position: absolute; top: 990px; left: 0; width: 856px; display: flex; justify-content: center; align-items: center; gap: 16px; }
  .brand-mark { width: 96px; height: 96px; border-radius: 50%; background: var(--brand-green); }
  .brand-text { display: flex; flex-direction: column; align-items: center; }
  .brand-name { font-weight: 700; font-size: 46px; color: var(--brand-blue); line-height: 1; }
  .brand-sub { font-size: 20px; color: var(--brand-green); margin-top: 6px; }

  .contact { position: absolute; top: 1128px; left: 0; width: 856px; text-align: center; font-size: 29px; color: var(--ink); }
  .contact b { font-weight: 700; color: var(--ink-strong); }
</style>
</head>
<body>
<main class="flyer">
  <div class="hero-photo" role="img" aria-label="Photo of a sunny blue sky over a white house with a red tiled roof covered in solar panels, yellow flowers and a butterfly in the foreground"></div>

  <p class="service-line">MAINTENANCE, CLEANING AND SAFETY CHECKS</p>

  <h1 class="headline">
    <span class="word-home">home</span>
    <span class="word-solar">solar</span>
    <span class="word-power">power</span>
    <span class="word-systems">systems</span>
  </h1>

  <ul class="benefits">
    <li class="benefit benefit-free"><span><b>FREE ELECTRICITY</b><br><b>with help from</b><br><b>the SUN</b></span></li>
    <li class="benefit benefit-affordable"><span><b>AFFORDABLE</b> Premium<br><b>SOLAR SOLUTIONS</b><br>tailored for you</span></li>
    <li class="benefit benefit-bills"><span><b>WIPE OUT</b> your <b>ELECTRICITY</b><br><b>BILLS &amp; PROTECT AGAINST</b><br>future electricity <b>PRICE RICES</b></span></li>
    <li class="benefit benefit-emissions"><span><b>SAVE TONNES</b> of<br>greenhouse<br><b>GAS EMISSIONS</b></span></li>
  </ul>

  <div class="brand">
    <div class="brand-mark"></div>
    <div class="brand-text">
      <span class="brand-name">Dorrit &amp; Vale</span>
      <span class="brand-sub">Solar and Electrical Contractors</span>
    </div>
  </div>

  <p class="contact">CALL NOW: <b>0491638274</b> or visit: <b>www.dorritandvale.com.au</b></p>
</main>
</body>
</html>
```